Business cards for the RL Group

We are looking for a template for our new business cards for our company that we can edit ourselves.
You will find our company colors in the logo. the logo on the back and on the front
first name Last Name
position
E-mail address
mobile number
landline number
Companies we have 2 RL Sicherheit GmbH and RL Services GmbH
address
Lindenbergweg 42
22459 Hamburg
www.rlgruppe-nord.de

Something modern, simple but professional

if you have any questions, bring it on.

Sicherheit

Steht in der Beschreibung

F0912C
F2A743
F7CA91
FBE8D2
FDF5EE

• recognition value
• professional
• Playful

```html
<!DOCTYPE html>
<html lang="de">
<head>
<meta charset="utf-8">
<title>RL Gruppe – Visitenkarten</title>
<link href="https://fonts.googleapis.com/css2?family=Montserrat:wght@400;500;700;800&display=swap" rel="stylesheet">
<style>
  :root {
    --backdrop: #8c8c8c;
    --card: #ffffff;
    --orange: #f5820d;
    --charcoal: #4f4f4f;
    --ink: #2b2b2b;
    --shadow: rgba(0, 0, 0, 0.28);
  }
  * { box-sizing: border-box; margin: 0; padding: 0; }
  html, body {
    width: 1200px;
    height: 1056px;
    overflow: hidden;
    background: var(--backdrop);
    font-family: "Montserrat", sans-serif;
  }
  .sheet {
    position: relative;
    width: 1200px;
    height: 1056px;
  }
  .card {
    position: absolute;
    left: 290px;
    width: 620px;
    height: 354px;
    background: var(--card);
    box-shadow: 0 10px 28px var(--shadow);
    overflow: hidden;
  }
  .card--front { top: 150px; }
  .card--back { top: 560px; }

  /* Front */
  .person {
    position: absolute;
    left: 48px;
    top: 44px;
  }
  .person__name {
    color: var(--orange);
    font-weight: 800;
    font-size: 30px;
    letter-spacing: 0.5px;
    text-transform: uppercase;
    line-height: 1;
  }
  .person__role {
    color: var(--ink);
    font-weight: 500;
    font-size: 18px;
    margin-top: 6px;
  }
  .person__rule {
    width: 132px;
    height: 3px;
    background: var(--orange);
    margin-top: 8px;
  }
  .address {
    position: absolute;
    left: 48px;
    top: 168px;
    color: var(--ink);
    font-size: 13.5px;
    font-weight: 500;
    line-height: 1.35;
  }
  .contacts {
    position: absolute;
    left: 48px;
    top: 222px;
    list-style: none;
  }
  .contacts__item {
    display: flex;
    align-items: center;
    gap: 8px;
    color: var(--ink);
    font-size: 14px;
    font-weight: 500;
    height: 26px;
  }
  .contacts__icon {
    width: 18px;
    height: 18px;
    flex: none;
  }

  /* Back */
  .brand {
    position: absolute;
    left: 0;
    right: 0;
    top: 118px;
    display: flex;
    justify-content: center;
    align-items: center;
    gap: 14px;
  }
  .brand__dot {
    width: 22px;
    height: 22px;
    border-radius: 50%;
    background: var(--orange);
  }
  .brand__name {
    color: var(--charcoal);
    font-weight: 800;
    font-size: 52px;
    letter-spacing: 1px;
    text-transform: uppercase;
  }
  .stripe {
    position: absolute;
    left: 0;
    bottom: 0;
    width: 620px;
    height: 354px;
  }
</style>
</head>
<body>
<main class="sheet">

  <section class="card card--front" aria-label="Vorderseite">
    <div class="person">
      <h1 class="person__name">Mara Lindholm</h1>
      <p class="person__role">Director / CEO</p>
      <div class="person__rule"></div>
    </div>

    <p class="address">Lindenbergweg 42<br>22459 Hamburg</p>

    <ul class="contacts">
      <li class="contacts__item">
        <svg class="contacts__icon" viewBox="0 0 18 18" aria-hidden="true">
          <rect width="18" height="18" rx="2" fill="var(--orange)"/>
          <rect x="6" y="3" width="6" height="12" rx="1.2" fill="none" stroke="#fff" stroke-width="1.5"/>
          <circle cx="9" cy="12.6" r="0.9" fill="#fff"/>
        </svg>
        (0)176-555120 40
      </li>
      <li class="contacts__item">
        <svg class="contacts__icon" viewBox="0 0 18 18" aria-hidden="true">
          <rect width="18" height="18" rx="2" fill="var(--orange)"/>
          <path d="M5 3.5 L7.5 3.5 L8.3 6.5 L6.8 7.6 C7.6 9.4 8.7 10.5 10.4 11.3 L11.5 9.8 L14.5 10.6 L14.5 13 C14.5 13.8 13.8 14.5 13 14.5 C7.8 14.2 3.8 10.2 3.5 5 C3.5 4.2 4.2 3.5 5 3.5 Z" fill="#fff"/>
        </svg>
        040 555318
      </li>
      <li class="contacts__item">
        <svg class="contacts__icon" viewBox="0 0 18 18" aria-hidden="true">
          <rect width="18" height="18" rx="2" fill="var(--orange)"/>
          <rect x="3.5" y="5" width="11" height="8" fill="none" stroke="#fff" stroke-width="1.4"/>
          <path d="M3.5 5 L9 9.6 L14.5 5" fill="none" stroke="#fff" stroke-width="1.4"/>
        </svg>
        info@rlgruppe-nord.com
      </li>
      <li class="contacts__item">
        <svg class="contacts__icon" viewBox="0 0 18 18" aria-hidden="true">
          <rect width="18" height="18" rx="2" fill="var(--orange)"/>
          <path d="M5.5 3.5 L5.5 13.5 L8 11 L9.8 14.6 L11.3 13.9 L9.5 10.4 L13 10.4 Z" fill="#fff"/>
        </svg>
        www.rlgruppe-nord.de
      </li>
    </ul>
  </section>

  <section class="card card--back" aria-label="Rückseite">
    <div class="brand">
      <span class="brand__dot"></span>
      <span class="brand__name">RL Gruppe</span>
    </div>
    <svg class="stripe" viewBox="0 0 620 354" aria-hidden="true">
      <polygon points="110,296 330,296 316,306 110,306" fill="var(--orange)"/>
      <polygon points="334,290 556,272 556,281 322,300" fill="var(--charcoal)"/>
    </svg>
  </section>

</main>
</body>
</html>
```